Electrical panel service sticker w Bucket truck & Logo

We have a rather plain sticker we put on lighting panels to remind customers who to call for service. We want to redesign them with brushed aluminum background. We want a remake of the sticker with the outline of a bucket truck. You'll need to find or draw the outling of a bucket truck maybe with the boom up slightly as we will get these stickers die cut.

We want LOGO with Ph.# and Email.
Electrical * Lighting * Sign Service

Target Market(s)

Commercial property managers

Industry/Entity Type

Property Management

Requirements
Must have
• Bucket Truck Outline

```html
<!DOCTYPE html>
<html lang="en">
<head>
<meta charset="utf-8">
<title>Glowline Facilities – Panel Service Sticker</title>
<link rel="stylesheet" href="https://fonts.googleapis.com/css2?family=Oswald:wght@600;700&family=Lato:wght@700&display=swap">
<style>
  :root {
    --page: #ffffff;
    --metal-light: #dcdcdc;
    --metal-mid: #cfcfcf;
    --brand-red: #c21f2f;
    --brand-blue: #1d3f95;
  }
  html, body {
    margin: 0;
    padding: 0;
    width: 1200px;
    height: 960px;
    overflow: hidden;
    background: var(--page);
  }
  .canvas {
    position: relative;
    width: 1200px;
    height: 960px;
  }
  .sticker {
    position: absolute;
    left: 47px;
    top: 196px;
    width: 1103px;
    height: 567px;
    background: linear-gradient(180deg, var(--metal-light) 0%, var(--metal-mid) 50%, var(--metal-light) 100%);
  }
  .sticker-frame {
    position: absolute;
    left: 29px;
    top: 30px;
    width: 1040px;
    height: 502px;
    border: 3px solid var(--brand-blue);
  }
  .brand-name {
    position: absolute;
    left: 53px;
    top: 52px;
    margin: 0;
    font-family: "Oswald", sans-serif;
    font-weight: 700;
    font-size: 118px;
    line-height: 118px;
    letter-spacing: 1px;
    text-transform: uppercase;
    color: var(--brand-red);
  }
  .brand-name span { display: block; }
  .truck-art {
    position: absolute;
    left: 677px;
    top: 60px;
    width: 352px;
    height: 230px;
  }
  .phone {
    position: absolute;
    left: 0;
    right: 0;
    top: 304px;
    margin: 0;
    text-align: center;
    font-family: "Oswald", sans-serif;
    font-weight: 700;
    font-size: 112px;
    line-height: 120px;
    letter-spacing: 2px;
    color: var(--brand-blue);
  }
  .email, .services {
    position: absolute;
    left: 0;
    right: 0;
    margin: 0;
    text-align: center;
    font-family: "Lato", sans-serif;
    font-weight: 700;
    color: var(--brand-blue);
  }
  .email {
    top: 432px;
    font-size: 34px;
    line-height: 44px;
  }
  .services {
    top: 486px;
    font-size: 38px;
    line-height: 44px;
    text-transform: uppercase;
  }
</style>
</head>
<body>
<main class="canvas">
  <section class="sticker">
    <div class="sticker-frame"></div>
    <h1 class="brand-name"><span>Glowline</span><span>Facilities</span></h1>
    <svg class="truck-art" viewBox="0 0 352 230" role="img" aria-label="Red outline illustration of a bucket truck with its boom raised">
      <rect x="0" y="0" width="352" height="230" fill="#c9a3a6"/>
    </svg>
    <p class="phone">800-555-0147</p>
    <p class="email">service@glowlinefacilities.com</p>
    <p class="services">Electrical * Lighting * Sign Service</p>
  </section>
</main>
</body>
</html>
```